Upscale business cards needed for family office

We would like professional business cards created for employees of our family office. Relatively simple and straightforward, but also with a unique element to set them apart. Probably stick with neutral and simple colors that mesh well with the colors in the logo. We need space for the traditional elements, including name, title, address, email/phone number.

Industry/Entity Type

Business

Contact Information for Business Card

Space for name, title, phone number, email, address

```html
<!DOCTYPE html>
<html lang="en">
<head>
<meta charset="UTF-8">
<title>Harbor &amp; Lane — Business Card</title>
<link rel="stylesheet" href="https://fonts.googleapis.com/css2?family=Lato:wght@400;700;900&display=swap">
<style>
  :root {
    --backdrop: #2b2b2b;
    --card: #f7f7f7;
    --card-shade: #e9e9e9;
    --ink: #2f2f2f;
    --ink-soft: #3c3c3c;
    --icon: #4a4a4a;
    --band-dark: #0d0d0d;
    --band-grey: #6d6d6d;
    --brand-square: #3f78b5;
  }
  * { box-sizing: border-box; margin: 0; padding: 0; }
  html, body {
    width: 1200px; height: 873px; overflow: hidden;
    background: var(--backdrop);
    font-family: "Lato", sans-serif;
  }
  .business-card {
    position: absolute; left: 180px; top: 196px;
    width: 840px; height: 480px;
    background:
      repeating-linear-gradient(135deg, rgba(0,0,0,0.012) 0 2px, transparent 2px 5px),
      linear-gradient(160deg, #ffffff 0%, var(--card) 55%, var(--card-shade) 100%);
    overflow: hidden;
  }
  .brand {
    position: absolute; left: 62px; top: 66px;
    display: flex; align-items: center; gap: 14px;
  }
  .brand-square {
    width: 26px; height: 26px; background: var(--brand-square);
  }
  .brand-name {
    font-size: 30px; font-weight: 700; color: var(--ink);
    letter-spacing: 0.5px;
  }
  .holder {
    position: absolute; right: 80px; top: 70px; text-align: right;
  }
  .holder-name { font-size: 27px; font-weight: 900; color: var(--ink); }
  .holder-title { font-size: 17px; font-weight: 400; color: var(--ink-soft); margin-top: 2px; }
  .contacts {
    position: absolute; left: 70px; top: 300px;
    list-style: none;
  }
  .contacts li {
    display: flex; align-items: center; gap: 14px;
    font-size: 19px; font-weight: 700; color: var(--ink-soft);
    height: 34px; margin-bottom: 6px;
  }
  .contact-icon { width: 26px; height: 26px; flex: none; }
  .band-dark {
    position: absolute; left: 0; right: 0; bottom: 38px; height: 10px;
    background: var(--band-dark);
  }
  .band-grey {
    position: absolute; left: 0; right: 0; bottom: 0; height: 38px;
    background: var(--band-grey);
  }
</style>
</head>
<body>
  <section class="business-card">
    <div class="brand">
      <span class="brand-square"></span>
      <span class="brand-name">Harbor &amp; Lane</span>
    </div>

    <div class="holder">
      <p class="holder-name">Noah R. Calder</p>
      <p class="holder-title">President</p>
    </div>

    <ul class="contacts">
      <li>
        <svg class="contact-icon" viewBox="0 0 26 26" aria-hidden="true">
          <circle cx="13" cy="13" r="13" fill="var(--icon)"/>
          <path d="M7 11c0-2 3-3.5 6-3.5s6 1.5 6 3.5h-3v-1.5h-6V11z" fill="#fff"/>
          <rect x="8.5" y="12.5" width="9" height="6" rx="1" fill="#fff"/>
        </svg>
        <span>555.204.6170</span>
      </li>
      <li>
        <svg class="contact-icon" viewBox="0 0 26 26" aria-hidden="true">
          <circle cx="13" cy="13" r="13" fill="var(--icon)"/>
          <rect x="7" y="8.5" width="12" height="9" rx="1" fill="#fff"/>
          <path d="M7.5 9.5l5.5 4.5 5.5-4.5" fill="none" stroke="var(--icon)" stroke-width="1.3"/>
        </svg>
        <span>noah@harborlane.us</span>
      </li>
      <li>
        <svg class="contact-icon" viewBox="0 0 26 26" aria-hidden="true">
          <circle cx="13" cy="13" r="13" fill="var(--icon)"/>
          <path d="M13 6.5a4.5 4.5 0 0 0-4.5 4.5c0 3.5 4.5 8.5 4.5 8.5s4.5-5 4.5-8.5A4.5 4.5 0 0 0 13 6.5z" fill="#fff"/>
          <circle cx="13" cy="11" r="1.7" fill="var(--icon)"/>
        </svg>
        <span>Two Harbor Square, 12th Floor, Newport, RI 02840</span>
      </li>
    </ul>

    <div class="band-dark"></div>
    <div class="band-grey"></div>
  </section>
</body>
</html>
```